Plumtree Crate Society - New Website Design

Create a professional website for strawberries of the month club; a subscription box business that will INCLUDE dipped strawberries - some with sprinkles. Check out: http://www.orchardnook.com for examples. Our website URL will be www.PlumtreeCrateSociety.com
Please see wimplesack.com; fudgeguild.com and gruffcase.com for the concept I am after. The business has not been launched yet, I am currently in the pre-launch stage using a specialized landing page website, and so the time scale for developing my professional looking website is up to 1-2 weeks.
The webpage should have a fun feel and should match the style of the company logo at fudgeguild.com or gruffcase.com. The pages to include are 'Home', 'About us' and 'Get Started'
Thank you and good luck!

```html
<!DOCTYPE html>
<html lang="en">
<head>
<meta charset="utf-8">
<title>Plumtree Crate Society</title>
<link rel="stylesheet" href="https://fonts.googleapis.com/css2?family=Poppins:wght@300;400;500;600;700&display=swap">
<style>
:root{
  --red:#f2475b;
  --purple:#8d5cf6;
  --purple-soft:#a57df8;
  --pink:#f7e2e1;
  --green:#3fbf6f;
  --orange:#f7a21b;
  --ink:#1d1d1f;
  --grey:#8c8c8c;
  --light:#f5f5f5;
  --footer:#37414a;
  --footer-text:#a9b0b6;
  --white:#fff;
}
*{margin:0;padding:0;box-sizing:border-box}
html,body{width:1200px;height:2946px;overflow:hidden}
body{font-family:'Poppins',sans-serif;color:var(--ink);background:var(--white);position:relative}
.abs{position:absolute}
.site-header{position:absolute;left:0;top:0;width:1200px;height:88px;background:var(--white)}
.nav{position:absolute;left:88px;top:34px;display:flex;gap:36px;font-size:12px;font-weight:500;text-transform:uppercase}
.nav a{color:var(--ink);text-decoration:none;position:relative}
.nav a.active{color:var(--red)}
.nav a.active::before{content:"";position:absolute;left:0;top:-34px;width:100%;height:4px;background:var(--red)}
.brand{position:absolute;left:468px;top:26px;display:flex;align-items:center;gap:10px;font-size:22px;font-weight:600;color:#6b6b6b}
.brand-dot{width:30px;height:30px;border-radius:50%;background:var(--purple)}
.header-icons{position:absolute;right:80px;top:32px;display:flex;gap:26px}
.hero{position:absolute;left:0;top:88px;width:1200px;height:472px;background:var(--pink);overflow:hidden}
.hero-title{position:absolute;left:92px;top:180px;font-size:42px;line-height:52px;font-weight:600;color:var(--red)}
.slide-count{position:absolute;left:26px;top:154px;transform:rotate(-90deg);transform-origin:center;font-size:11px;font-weight:600;letter-spacing:1px}
.slide-line{position:absolute;left:42px;top:220px;width:2px;height:60px;background:var(--ink)}
.slide-dot{position:absolute;left:37px;width:11px;height:11px;border-radius:50%;border:2px solid var(--ink)}
.slide-dot.faint{border-color:var(--grey)}
.scroll-down{position:absolute;left:578px;top:538px;width:44px;height:44px;border-radius:50%;background:var(--white);box-shadow:0 4px 12px rgba(0,0,0,.08);display:flex;align-items:center;justify-content:center}
.section-title{position:absolute;left:0;width:1200px;text-align:center;font-size:27px;font-weight:500}
.section-rule{position:absolute;left:580px;width:40px;height:1px;background:#cfcfcf}
.step{position:absolute;width:300px;text-align:center}
.step-icon{width:88px;height:80px;margin:0 auto;border-radius:40px 40px 44px 44px;background:var(--white);box-shadow:0 10px 20px rgba(0,0,0,.07);display:flex;align-items:center;justify-content:center}
.step h3{font-size:15px;font-weight:400;margin-top:26px}
.step p{font-size:11.5px;color:var(--grey);line-height:22px;margin-top:6px}
.step-arrow{position:absolute;width:26px;height:26px;border-radius:50%;background:#eeeeee;display:flex;align-items:center;justify-content:center}
.plans{position:absolute;left:0;top:1002px;width:1200px;height:632px;background:var(--light)}
.plan{position:absolute;background:var(--white);text-align:center}
.plan h3{font-size:19px;font-weight:400;margin-top:36px}
.plan .price{font-size:32px;font-weight:600;margin-top:2px;line-height:40px}
.plan .price span{font-size:19px;font-weight:400}
.plan .ship{font-size:10px;margin-top:4px}
.plan .photo{margin:14px auto 0;border-radius:50%}
.btn{display:inline-block;border-radius:24px;font-size:11px;font-weight:500;text-transform:uppercase;line-height:44px}
.btn-outline{width:138px;border:1px solid #dedede;box-shadow:0 4px 10px rgba(0,0,0,.06);color:var(--ink)}
.btn-fill{width:154px;background:var(--red);color:var(--white);line-height:48px}
.quote{position:absolute;left:236px;top:1776px;width:728px;text-align:center;font-size:12px;line-height:22px;color:var(--grey)}
.quote-name{position:absolute;left:0;top:1862px;width:1200px;text-align:center;font-size:13px;font-weight:500;text-transform:uppercase}
.avatar{position:absolute;top:1909px;width:52px;height:52px;border-radius:50%}
.gallery-tile{position:absolute}
.footer{position:absolute;left:0;top:2534px;width:1200px;height:412px;background:var(--footer);color:var(--white)}
.newsletter{position:absolute;left:167px;top:2492px;width:866px;height:108px;border-radius:54px;background:var(--purple)}
.newsletter h2{position:absolute;left:48px;top:38px;font-size:22px;font-weight:400;color:var(--white)}
.news-field{position:absolute;left:222px;top:34px;width:462px;height:42px;border-radius:21px;background:var(--purple-soft);color:var(--white);font-size:12px;line-height:42px;padding-left:38px}
.news-btn{position:absolute;left:702px;top:32px;width:122px;height:46px;border-radius:23px;background:var(--white);font-size:12px;font-weight:600;text-align:center;line-height:46px}
.foot-col{position:absolute;top:2658px}
.foot-col h4{font-size:17px;font-weight:400;margin-bottom:18px}
.foot-col li{list-style:none;font-size:12px;color:var(--footer-text);line-height:36px;display:flex;align-items:flex-start;gap:10px}
.foot-col li i{display:inline-block;width:9px;height:9px;margin-top:13px;border-radius:2px;background:var(--red)}
.foot-col li b{display:inline-block;width:9px;height:9px;margin-top:13px;border-radius:2px;background:var(--footer-text)}
.copy{position:absolute;left:0;top:2908px;width:1200px;text-align:center;font-size:12px;color:var(--white)}
.to-top{position:absolute;left:1139px;top:2869px;width:36px;height:36px;border-radius:50%;background:var(--white);display:flex;align-items:center;justify-content:center}
</style>
</head>
<body>

<header class="site-header">
  <nav class="nav"><a class="active" href="#">Home</a><a href="#">About us</a><a href="#">Get started</a></nav>
  <div class="brand"><span class="brand-dot"></span>Plumtree Crate Society</div>
  <div class="header-icons">
    <svg width="20" height="20" viewBox="0 0 20 20" fill="none" stroke="#333" stroke-width="1.6"><circle cx="8" cy="8" r="6"/><path d="M13 13l5 5"/></svg>
    <svg width="20" height="20" viewBox="0 0 20 20" fill="none" stroke="#333" stroke-width="1.6"><circle cx="10" cy="6" r="4"/><path d="M2 19c1-5 15-5 16 0"/></svg>
    <svg width="24" height="22" viewBox="0 0 24 22" fill="none" stroke="#333" stroke-width="1.6"><path d="M1 3h3l3 11h11l2-8H6"/><circle cx="8" cy="18" r="1.5"/><circle cx="17" cy="18" r="1.5"/><circle cx="20" cy="4" r="4" fill="#f2475b" stroke="none"/></svg>
  </div>
</header>

<section class="hero">
  <svg class="abs" style="left:0;top:0" width="1200" height="472" viewBox="0 0 1200 472">
    <path d="M1030 0H1200V210L1125 260Z" fill="#f2475b"/>
    <path d="M690 0H1080L800 300C740 360 640 350 600 300C560 250 560 190 600 140Z" fill="#8d5cf6"/>
  </svg>
  <div class="abs" role="img" aria-label="White plate of chocolate and pink dipped strawberries with sprinkles" style="left:650px;top:64px;width:420px;height:290px;border-radius:50%;background:radial-gradient(circle at 50% 45%,#e8a6c4 0%,#6b3a2a 45%,#f4f1f1 72%,#ffffff 100%)"></div>
  <h1 class="hero-title">Strawberries<br>of the month club</h1>
  <div class="slide-count">01 / 03</div>
  <div class="slide-line"></div>
  <div class="slide-dot" style="top:261px"></div>
  <div class="slide-dot faint" style="top:286px"></div>
  <div class="slide-dot faint" style="top:310px"></div>
  <svg class="abs" style="left:1144px;top:212px" width="22" height="42" viewBox="0 0 22 42" fill="none" stroke-width="2.2"><path d="M4 10l7-7 7 7" stroke="#888"/><path d="M4 32l7 7 7-7" stroke="#222"/></svg>
</section>
<div class="scroll-down"><svg width="12" height="14" viewBox="0 0 12 14" fill="none" stroke="#222" stroke-width="1.6"><path d="M6 1v12M1 8l5 5 5-5"/></svg></div>

<div class="section-rule" style="top:654px"></div>
<h2 class="section-title" style="top:658px">How it Works</h2>

<div class="step" style="left:111px;top:736px">
  <div class="step-icon"><svg width="30" height="36" viewBox="0 0 30 36" fill="none" stroke="#8d5cf6" stroke-width="1.8"><path d="M2 2h18l8 8v24H2z"/><path d="M8 14h14M8 20h14M8 26h10" stroke="#f2475b"/></svg></div>
  <h3>Choose your plan</h3>
  <p>Quisque rutrum aenean imperdiet etiamics<br>ultricies nisi vel augue.</p>
</div>
<div class="step-arrow" style="left:417px;top:764px"><svg width="8" height="10" viewBox="0 0 8 10" fill="none" stroke="#555" stroke-width="1.5"><path d="M2 1l4 4-4 4"/></svg></div>
<div class="step" style="left:449px;top:736px">
  <div class="step-icon"><svg width="38" height="34" viewBox="0 0 38 34" fill="none" stroke="#3fbf6f" stroke-width="1.8"><rect x="2" y="5" width="34" height="27" rx="2"/><path d="M2 12h34M10 2v6M28 2v6"/><circle cx="19" cy="22" r="5" stroke="#f7a21b"/></svg></div>
  <h3>Receive your monthly box</h3>
  <p>Quisque rutrum aenean imperdiet etiamics<br>ultricies nisi vel augue.</p>
</div>
<div class="step-arrow" style="left:755px;top:764px"><svg width="8" height="10" viewBox="0 0 8 10" fill="none" stroke="#555" stroke-width="1.5"><path d="M2 1l4 4-4 4"/></svg></div>
<div class="step" style="left:793px;top:736px">
  <div class="step-icon"><svg width="28" height="36" viewBox="0 0 28 36" fill="none" stroke="#f2475b" stroke-width="1.8"><path d="M14 10C4 8 2 16 4 22c2 6 7 11 10 12 3-1 8-6 10-12 2-6 0-14-10-12z"/><path d="M9 4l5 5 5-5" stroke="#3fbf6f"/></svg></div>
  <h3>Enjoy your Strawberries</h3>
  <p>Quisque rutrum aenean imperdiet etiamics<br>ultricies nisi vel augue.</p>
</div>

<section class="plans">
  <div class="section-rule" style="top:60px"></div>
  <h2 class="section-title" style="top:66px">Choose your Plan</h2>
  <div class="plan" style="left:88px;top:135px;width:301px;height:391px">
    <h3>Monthly Plan</h3>
    <div class="price" style="color:var(--green)">$29.99<span>/month</span></div>
    <div class="ship">(PLUS SHIPPING)</div>
    <div class="photo" role="img" aria-label="Single strawberry dipped in dark chocolate" style="width:120px;height:150px;background:radial-gradient(circle at 50% 35%,#d8262f 0%,#b31c24 45%,#4a2418 75%,#fff 100%)"></div>
    <div style="margin-top:18px"><span class="btn btn-outline">Get started</span></div>
  </div>
  <div class="plan" style="left:436px;top:135px;width:330px;height:432px">
    <h3 style="margin-top:40px">6 Month Plan</h3>
    <div class="price" style="color:var(--red)">$24.99<span>/month</span></div>
    <div class="ship">(PLUS SHIPPING)</div>
    <div class="photo" role="img" aria-label="Two chocolate dipped strawberries with white drizzle" style="width:150px;height:150px;margin-top:28px;background:radial-gradient(circle at 50% 50%,#5a3022 0%,#3b1e14 50%,#fff 75%)"></div>
    <div style="margin-top:50px"><span class="btn btn-fill">Get started</span></div>
  </div>
  <div class="plan" style="left:811px;top:135px;width:301px;height:391px">
    <h3>12 Month Plan</h3>
    <div class="price" style="color:var(--orange)">$21.99<span>/month</span></div>
    <div class="ship">(PLUS SHIPPING)</div>
    <div class="photo" role="img" aria-label="Bowl of pink and chocolate dipped strawberries with sprinkles" style="width:190px;height:150px;background:radial-gradient(circle at 50% 45%,#e9a3c3 0%,#6a3626 42%,#f2f0f0 70%,#fff 100%)"></div>
    <div style="margin-top:18px"><span class="btn btn-outline">Get started</span></div>
  </div>
</section>

<div class="section-rule" style="top:1706px"></div>
<h2 class="section-title" style="top:1716px">Customer Testimonials</h2>
<svg class="abs" style="left:200px;top:1766px" width="30" height="24" viewBox="0 0 30 24" fill="#e4e4e4"><path d="M0 24V12C0 4 5 0 12 0v5c-4 0-6 3-6 7h6v12zM16 24V12c0-8 5-12 12-12v5c-4 0-6 3-6 7h6v12z"/></svg>
<p class="quote">Lorem ipsum dolor sit amet consectetuer adipiscing elit aenean commodo ligula eget dolor aenean massa cum sociis natoque penatibus et magnis dis parturient montes nascetur ridiculus mus donec quam felis ultricies nec pellentesque eu pretium quis sem lorem ipsum dolor.</p>
<svg class="abs" style="left:664px;top:1818px" width="30" height="24" viewBox="0 0 30 24" fill="#e4e4e4"><path d="M30 0v12c0 8-5 12-12 12v-5c4 0 6-3 6-7h-6V0zM14 0v12c0 8-5 12-12 12v-5c4 0 6-3 6-7H2V0z"/></svg>
<div class="quote-name">Margo Ellwyn</div>
<div class="avatar" role="img" aria-label="Customer portrait" style="left:418px;background:#d8cfc8;box-shadow:0 6px 14px rgba(0,0,0,.2);width:56px;height:56px;top:1907px"></div>
<div class="avatar" role="img" aria-label="Customer portrait" style="left:493px;background:#3a3a3a"></div>
<div class="avatar" role="img" aria-label="Customer portrait" style="left:573px;background:#e0b48f"></div>
<div class="avatar" role="img" aria-label="Customer portrait" style="left:652px;background:#4b6f5e"></div>
<div class="avatar" role="img" aria-label="Customer portrait" style="left:732px;background:#8a5bd6"></div>

<div class="section-rule" style="top:2030px"></div>
<h2 class="section-title" style="top:2036px">#Strawberries Subscription Snapgrid</h2>
<div class="gallery-tile" role="img" aria-label="Strawberries in a metal colander" style="left:88px;top:2103px;width:174px;height:156px;background:linear-gradient(135deg,#8a8a86,#c8282c)"></div>
<div class="gallery-tile" role="img" aria-label="Strawberries in a white bowl on wood" style="left:264px;top:2103px;width:172px;height:156px;background:linear-gradient(135deg,#c42a2f,#5a4136)"></div>
<div class="gallery-tile" role="img" aria-label="Punnets of fresh strawberries" style="left:88px;top:2262px;width:174px;height:156px;background:linear-gradient(135deg,#d3262c,#9c1d22)"></div>
<div class="gallery-tile" role="img" aria-label="Strawberries in a yellow bowl" style="left:264px;top:2262px;width:172px;height:156px;background:radial-gradient(circle,#f0c21c 30%,#2a3c48 80%)"></div>
<div class="gallery-tile" role="img" aria-label="Strawberries in a woven basket on a checked cloth" style="left:438px;top:2103px;width:674px;height:315px;background:linear-gradient(100deg,#c81f27 0%,#b0161e 45%,#b88b5c 75%,#e2d9cf 100%)"></div>

<footer class="footer">
  <svg class="abs" style="left:0;top:-36px" width="1200" height="37" viewBox="0 0 1200 37"><path d="M0 37V35C400 -10 800 -10 1200 35V37Z" fill="#37414a"/></svg>
</footer>
<div class="abs" style="left:0;top:2498px;width:1200px;height:40px;background:linear-gradient(#fff,#fff)"></div>
<svg class="abs" style="left:0;top:2498px" width="1200" height="72" viewBox="0 0 1200 72"><path d="M0 72V70C350 20 850 20 1200 70V72Z" fill="#37414a"/></svg>
<div class="newsletter">
  <h2>Newsletter</h2>
  <div class="news-field">Enter your email address</div>
  <svg class="abs" style="left:236px;top:50px" width="14" height="10" viewBox="0 0 14 10" fill="none" stroke="#fff" stroke-width="1.2"><rect x="1" y="1" width="12" height="8"/><path d="M1 1l6 5 6-5"/></svg>
  <div class="news-btn">SUBMIT</div>
</div>

<div class="foot-col" style="left:88px;color:#fff">
  <h4>Quick Links</h4>
  <ul><li>› Home</li><li>› About us</li><li>› Get Started</li></ul>
</div>
<div class="foot-col" style="left:410px;color:#fff">
  <h4>Contact</h4>
  <ul><li><i></i>+123 555 0142</li><li><i></i>hello@plumtreecrate.com</li><li><i style="border-radius:50%"></i><span style="line-height:22px;padding-top:7px">6:30am - 5:00pm PT<br>(Monday - Friday)</span></li></ul>
</div>
<div class="foot-col" style="left:827px;color:#fff">
  <h4>Follow us on socail media</h4>
  <ul><li><b></b>Friendfold</li><li><b style="background:var(--red)"></b><span style="color:var(--red)">Chirpline</span></li><li><b></b>Pinboardly</li><li><b></b>Snapgrid</li></ul>
</div>
<div class="foot-col" style="left:939px;top:2698px;color:#fff">
  <ul><li><b></b>Reelcast</li><li><b></b>Workmesh</li></ul>
</div>
<p class="copy">© 2017, All Rights Reserved.</p>
<div class="to-top"><svg width="12" height="14" viewBox="0 0 12 14" fill="none" stroke="#222" stroke-width="1.6"><path d="M6 13V1M1 6l5-5 5 5"/></svg></div>

</body>
</html>
```